Modern Catering Company needs Letterhead Design

We need a letterhead design that will make effective use of the corporate logo and color scheme, along with careful typography, helps this letterhead design communicate the brand well. We do have a corporate logo, however feel free to enhance the color scheme with gold and purple. We are serving a very upscale clientele so the letterhead has to reflect elegance, professionalism, cleanliness, and modern style. We are branding the company so the letterhead and business cards must fit the brand story. There should be no cartoonish elements in the design and we are looking for sharper lines.

Target Market(s)

Businesses and upscale clientele

Industry/Entity Type

Catering

Contact Information for Business Card

while this design can have any number of quirks and distinctions, it needs to be cohesive with the entire brand story clean, professional but edgy

Requirements
Must have
• must have good and carefully placement of it’s logo and where you place the text or the message. Colors blue, very deep purple, jewel tones not pastels, gold. Blue must be the primary color you may accent with purple or gold. Contact information is as follows: Co-Owners/ Chefs: R. Hollowell & T. Brenn, phone: 414-555-0182 email:Contact@emberoakcatering.example, address: 6172 W Larkmoor Ln, Milwaukee, WI 53299
Should not have
• pastel colors, Do not add the BBQ information to the letterhead or business card it was a mistake by the previous designer.

```html
<!DOCTYPE html>
<html lang="en">
<head>
<meta charset="utf-8">
<title>Ember Oak Catering – Business Card</title>
<link href="https://fonts.googleapis.com/css2?family=Open+Sans:wght@400;600&display=swap" rel="stylesheet">
<style>
  :root {
    --brand-blue: #0a6cf0;
    --band-dark: #333333;
    --card-white: #ffffff;
    --backdrop: #e9e7e4;
    --text-white: #ffffff;
  }
  * { box-sizing: border-box; margin: 0; padding: 0; }
  html, body {
    width: 1200px; height: 900px; overflow: hidden;
    background: var(--backdrop);
    font-family: "Open Sans", Arial, sans-serif;
  }
  .canvas { position: relative; width: 1200px; height: 900px; }

  .card {
    position: absolute;
    overflow: hidden;
    box-shadow: 0 6px 18px rgba(0,0,0,0.18);
  }
  .card-front { left: 78px; top: 34px; width: 588px; height: 364px; background: var(--card-white); }
  .card-back  { left: 388px; top: 505px; width: 567px; height: 352px; background: var(--brand-blue); }

  .card-shapes { position: absolute; inset: 0; }

  .brand {
    position: absolute;
    left: 0; right: 0;
    display: flex; align-items: center; justify-content: center; gap: 14px;
    font-weight: 400; font-size: 34px; letter-spacing: 2px;
    white-space: nowrap;
  }
  .card-front .brand { top: 68px; color: var(--brand-blue); }
  .card-back .brand  { top: 150px; color: var(--text-white); }
  .brand-square { width: 22px; height: 22px; flex: none; }
  .card-front .brand-square { background: var(--band-dark); }
  .card-back .brand-square  { background: var(--text-white); }

  .holder {
    position: absolute; right: 316px; top: 262px;
    text-align: right; color: var(--text-white);
    white-space: nowrap;
  }
  .holder-name { font-size: 18px; font-weight: 600; line-height: 24px; }
  .holder-title { font-size: 15px; line-height: 20px; }

  .contact-list {
    position: absolute; left: 293px; top: 250px;
    list-style: none; color: var(--text-white);
    font-size: 14px; line-height: 21px;
  }
  .contact-list li { display: flex; align-items: center; gap: 12px; white-space: nowrap; }
  .contact-icon { width: 12px; height: 12px; flex: none; }

  .address {
    position: absolute; left: 0; right: 0; top: 328px;
    text-align: center; color: var(--text-white);
    font-size: 15px; white-space: nowrap;
  }
</style>
</head>
<body>
<main class="canvas">

  <section class="card card-front" aria-label="Business card front">
    <svg class="card-shapes" width="588" height="364" viewBox="0 0 588 364" aria-hidden="true">
      <polygon points="0,199 404,199 382,223 0,223" fill="var(--band-dark)"/>
      <polygon points="0,228 382,228 415,191 588,191 588,364 0,364" fill="var(--brand-blue)"/>
    </svg>

    <div class="brand"><span class="brand-square"></span><span>EMBER OAK CATERING</span></div>

    <div class="holder">
      <p class="holder-name">R. Hollowell &amp; T. Brenn</p>
      <p class="holder-title">Co-Owners / Chefs</p>
    </div>

    <ul class="contact-list">
      <li>
        <svg class="contact-icon" viewBox="0 0 12 12" aria-hidden="true"><path d="M2 1l2.2-.3 1 2.6-1.3 1a6.5 6.5 0 0 0 3.3 3.3l1-1.3 2.6 1L11 10.5C10.5 11.2 9.6 11.4 8.8 11 5 9.5 2.5 7 1 3.2.6 2.4.9 1.5 2 1z" fill="currentColor"/></svg>
        <span>414-555-0182</span>
      </li>
      <li>
        <svg class="contact-icon" viewBox="0 0 12 12" aria-hidden="true"><rect x="1" y="3" width="10" height="7" fill="currentColor"/><path d="M1 3l5 4 5-4" stroke="var(--brand-blue)" stroke-width="1" fill="none"/></svg>
        <span>Contact@emberoakcatering.example</span>
      </li>
      <li>
        <svg class="contact-icon" viewBox="0 0 12 12" aria-hidden="true"><g fill="none" stroke="currentColor" stroke-width="1"><circle cx="6" cy="6" r="5"/><ellipse cx="6" cy="6" rx="2.2" ry="5"/><path d="M1 6h10M2 3.5h8M2 8.5h8"/></g></svg>
        <span>www.emberoakcatering.example</span>
      </li>
    </ul>

    <p class="address">6172 W Larkmoor Ln, Milwaukee, WI 53299</p>
  </section>

  <section class="card card-back" aria-label="Business card back">
    <div class="brand"><span class="brand-square"></span><span>EMBER OAK CATERING</span></div>
  </section>

</main>
</body>
</html>
```